The Seeds Of Quiet Harvest Inc.

On one side have the business name. On the other side have contact information. This is an indoor cannabis cultivation business. It’s a new company in Sacramento ca. So we need a logo designed. The company is Called the seeds of quiet harvest. We grow and distribute marijuana in California. We would like to see designers use the color green and communicate cultivation.

Target Market(s)

Networking

Contact Information for Business Card

Brent Tavaro: president
Phone: (916) 555-0147
Email: brent@theseedsofquietharvest.net

Logo Text

Not sure if i want text or just an image created by designers.

Font styles to use
Script

Colors
000000
9bcb3c
fbfcf7
cadf82

Requirements
Nice to have
• A classic elegant professional card.

```html
<!DOCTYPE html>
<html lang="en">
<head>
<meta charset="utf-8">
<title>The Seeds Of Quiet Harvest Inc. – Business Card</title>
<link rel="stylesheet" href="https://fonts.googleapis.com/css2?family=Open+Sans:wght@300;400;600;700&display=swap">
<style>
  :root {
    --backdrop: #1d1d1f;
    --card: #f3f3f4;
    --green: #9bcb3c;
    --olive: #8fae55;
    --ink: #000000;
    --grey: #4a4a4a;
    --white: #fbfcf7;
  }
  * { margin: 0; padding: 0; box-sizing: border-box; }
  html, body {
    width: 1131px; height: 1200px; overflow: hidden;
    background: var(--backdrop);
    font-family: "Open Sans", Arial, sans-serif;
  }
  .canvas { position: relative; width: 1131px; height: 1200px; }
  .card {
    position: absolute; left: 153px; width: 781px; height: 448px;
    background: var(--card); border-radius: 26px; overflow: hidden;
  }
  .card--front { top: 109px; }
  .card--back { top: 599px; height: 444px; }
  .wave { position: absolute; inset: 0; width: 100%; height: 100%; }
  .holder { position: absolute; left: 45px; top: 62px; }
  .holder__name { color: var(--green); font-size: 24px; font-weight: 400; }
  .holder__role { color: #333; font-size: 16px; margin-top: 4px; }
  .brand { position: absolute; text-align: center; }
  .brand__name {
    display: flex; align-items: center; justify-content: center; gap: 10px;
    color: var(--ink); font-weight: 700; letter-spacing: -0.5px;
  }
  .brand__dot { border-radius: 50%; background: var(--green); display: inline-block; }
  .brand__tag { color: var(--grey); font-weight: 400; }
  .card--front .brand { right: 40px; top: 128px; width: 300px; }
  .card--front .brand__name { font-size: 36px; }
  .card--front .brand__dot { width: 18px; height: 18px; }
  .card--front .brand__tag { font-size: 18px; margin-top: 4px; }
  .card--back .brand { left: 0; right: 0; top: 165px; }
  .card--back .brand__name { font-size: 52px; }
  .card--back .brand__dot { width: 24px; height: 24px; }
  .card--back .brand__tag { font-size: 24px; margin-top: 6px; }
  .address {
    position: absolute; left: 45px; top: 227px;
    color: var(--white); font-size: 20px; font-weight: 300; line-height: 28px;
  }
  .contacts { position: absolute; left: 58px; top: 327px; list-style: none; }
  .contacts li {
    display: flex; align-items: center; gap: 12px; height: 28px;
    color: var(--white); font-size: 16px; font-weight: 300;
  }
  .contacts svg { width: 14px; height: 14px; fill: var(--white); }
</style>
</head>
<body>
<div class="canvas">
  <section class="card card--front">
    <svg class="wave" viewBox="0 0 781 448" preserveAspectRatio="none" aria-hidden="true">
      <path fill="var(--ink)" d="M0,205 C120,168 260,162 400,212 C540,262 650,312 781,262 L781,448 L0,448 Z"/>
      <path fill="var(--olive)" d="M0,222 C130,186 270,184 400,232 C540,284 650,320 781,290 L781,448 L0,448 Z"/>
      <path fill="var(--green)" d="M0,228 C150,200 290,212 420,262 C560,318 660,388 781,384 L781,448 L0,448 Z"/>
    </svg>
    <div class="holder">
      <h1 class="holder__name">Brent Tavaro</h1>
      <p class="holder__role">president</p>
    </div>
    <div class="brand">
      <div class="brand__name"><span class="brand__dot"></span>Quiet Harvest</div>
      <p class="brand__tag">the seeds of quiet harvest</p>
    </div>
    <p class="address">Address &nbsp;city - State<br>Zip, Country</p>
    <ul class="contacts">
      <li><svg viewBox="0 0 24 24"><path d="M6.6 10.8a15.1 15.1 0 0 0 6.6 6.6l2.2-2.2c.3-.3.7-.4 1-.2 1.1.4 2.3.6 3.6.6.6 0 1 .4 1 1V20c0 .6-.4 1-1 1A17 17 0 0 1 3 4c0-.6.4-1 1-1h3.5c.6 0 1 .4 1 1 0 1.3.2 2.5.6 3.6.1.3 0 .7-.2 1z"/></svg>(916) 555-0147</li>
      <li><svg viewBox="0 0 24 24"><path d="M2 8c3-4 17-4 20 0l-1 3-4-1V7c-3-1-7-1-10 0v3l-4 1zM6 12h12l2 8H4z"/></svg>(916) 555-0147</li>
      <li><svg viewBox="0 0 24 24"><path d="M2 5h20v14H2zm2 2v.5l8 5 8-5V7z"/></svg>brent@theseedsofquietharvest.net</li>
    </ul>
  </section>

  <section class="card card--back">
    <div class="brand">
      <div class="brand__name"><span class="brand__dot"></span>Quiet Harvest</div>
      <p class="brand__tag">the seeds of quiet harvest</p>
    </div>
  </section>
</div>
</body>
</html>
```